Stand out flyer needed for Boxing gym

Hi we need a trifold brochure designed for our outdoor boxing business it will be delivered to doctors and nutritionists to help their patients be healthier and get fit.We have supplied high res pictures for you to use in the brochure. We need a design that use a lot of yellow so it captures their attention. You can check our website for design colours www.punchyard-fit.com.au

Target Market(s)

Overweight or unfit people looking to change their lives

Industry/Entity Type

Health And Wellness

Font styles to use
Sans Serif

Colors
fbee3d
ffffff
000000

Requirements
Must have
• (main heading - large bold font) Get fit lose weight & feel great
• (bold) Unlimited outdoor boxing classes $14.95
• Complete affordability & No judgements guaranteed
• (bold) Tailored programs (bold)
• Our programs are structured so that members of all fitness levels feel confident & comfortable during their start-up phase allowing you to quickly build your fitness
• (bold) Injury prevention (bold)
• Our training systems include techniques that will help you avoid injuries and build balanced strength
• (bold) Strengthen & Tone your core (bold)
• You're core muscles are some of you're most important muscles. Each workout you do incorporates core exercises to help avoid injuries and make you're total body stronger
• (bold) Wake up with more energy(bold)
• Every class you'll do will have you filled with energy the will pump you up for the rest of your day
• (bold) Sleep better(bold)
• One of the best parts of exercise is the benefit it has on your sleeping patterns. You'll sleep deeper & more sound
• (bold) Supportive environment (bold)
• At JAB YARD you'll be surrounded by trainers & other members who are there to encourage & motivate you to reach your goals and to get you moving more.
• Coupon code: SwingHigh27

```html
<!DOCTYPE html>
<html lang="en">
<head>
<meta charset="utf-8">
<title>JAB YARD – Trifold Brochure</title>
<link rel="stylesheet" href="https://fonts.googleapis.com/css2?family=Montserrat:wght@400;600;700;800;900&family=Open+Sans:wght@400;600&display=swap">
<style>
  :root{
    --yellow:#fbee3d;
    --yellow-deep:#e9dc22;
    --black:#000000;
    --charcoal:#2a2a2a;
    --white:#ffffff;
    --grey-text:#3a3a3a;
  }
  *{box-sizing:border-box;margin:0;padding:0}
  html,body{width:1200px;height:1200px;overflow:hidden}
  body{background:#f4f4f4;font-family:"Open Sans",Arial,sans-serif;position:relative}
  .sheet{position:absolute;left:30px;width:1140px;height:560px;box-shadow:0 6px 24px rgba(0,0,0,.18);overflow:hidden}
  .sheet--outside{top:30px}
  .sheet--inside{top:620px}
  .panel{position:absolute;top:0;width:380px;height:560px;overflow:hidden}
  .panel--1{left:0}.panel--2{left:380px}.panel--3{left:760px}
  .layer{position:absolute;inset:0;width:100%;height:100%}
  .heading{font-family:"Montserrat",Arial,sans-serif;font-weight:800;line-height:1.05}
  .abs{position:absolute}

  /* outside left */
  .programs__title{left:28px;top:168px;font-size:30px;color:var(--black);width:200px}
  .programs__rule{left:28px;top:156px;width:34px;height:3px;background:var(--black)}
  .programs__text{left:28px;top:240px;width:190px;font-size:12.5px;line-height:1.45;color:var(--black)}
  .contact__tab{left:200px;top:392px;background:var(--yellow);padding:7px 16px;font-family:"Montserrat",Arial,sans-serif;font-weight:800;font-size:17px;color:var(--black)}
  .contact__list{left:40px;top:440px;list-style:none;font-size:16px;color:var(--grey-text)}
  .contact__list li{display:flex;align-items:center;gap:10px;margin-bottom:9px}
  .contact__list svg{width:16px;height:16px;flex:none}

  /* outside middle */
  .offer{left:40px;top:70px;width:305px;text-align:center;color:var(--white)}
  .offer__lead{font-size:44px;font-weight:900}
  .offer__sub{font-family:"Montserrat",Arial,sans-serif;font-weight:700;font-size:15px;margin-top:2px}
  .offer__price{font-family:"Montserrat",Arial,sans-serif;font-weight:900;font-size:56px;color:var(--yellow);margin-top:6px}
  .offer__note{font-size:16px;line-height:1.35;margin-top:6px}
  .offer__dash{width:40px;height:4px;background:var(--yellow);margin:14px auto 0}
  .headline{left:40px;top:395px;width:305px;text-align:center;color:var(--white)}
  .headline__big{display:block;font-size:80px;font-weight:900;line-height:.95}
  .headline__small{display:block;font-size:19px;font-weight:800;margin-top:8px}

  /* cover */
  .brand{left:40px;top:112px;width:330px;display:flex;justify-content:center;align-items:center;gap:12px}
  .brand__mark{width:20px;height:20px;background:var(--black)}
  .brand__name{font-family:"Montserrat",Arial,sans-serif;font-weight:800;font-size:40px;color:var(--black);letter-spacing:2px}

  /* inside */
  .feature__title{font-size:21px}
  .feature__text{font-size:13.5px;line-height:1.4;margin-top:6px}
  .injury{left:26px;top:92px;width:330px;color:var(--black)}
  .core{left:26px;top:430px;width:330px;color:var(--white)}
  .core .feature__title{color:var(--yellow)}
  .energy{left:40px;top:34px;width:265px;color:var(--white)}
  .energy .feature__title,.sleep .feature__title{color:var(--yellow)}
  .sleep{left:40px;top:418px;width:240px;color:var(--white)}
  .signup{left:0;top:70px;width:380px;text-align:center;color:var(--black)}
  .signup__icon{width:44px;height:50px;margin:0 auto 10px;display:block}
  .signup__title{font-size:26px}
  .signup__rule{width:46px;height:3px;background:var(--black);margin:10px auto}
  .signup__label{font-family:"Montserrat",Arial,sans-serif;font-size:13px;letter-spacing:1px}
  .signup__code{font-size:34px;font-weight:900;margin-top:4px}
  .support__band{left:0;top:418px;width:230px;height:86px;background:var(--yellow);opacity:.92}
  .support__title{left:24px;top:428px;font-size:24px;color:var(--black);width:200px}
  .support__rule{left:140px;top:262px;width:1px;height:110px;background:var(--black)}
  .support__text{left:152px;top:250px;width:210px;font-size:12.5px;line-height:1.45;color:var(--black)}
</style>
</head>
<body>

<section class="sheet sheet--outside" aria-label="Brochure outside">

  <div class="panel panel--1">
    <svg class="layer" viewBox="0 0 380 560" role="img" aria-label="Photo of a city skyline and park in soft grey">
      <defs>
        <linearGradient id="cityTone" x1="0" y1="0" x2="0" y2="1"><stop offset="0" stop-color="#d8d8d8"/><stop offset="1" stop-color="#bdbdbd"/></linearGradient>
      </defs>
      <rect width="380" height="560" fill="url(#cityTone)"/>
    </svg>
    <svg class="layer" viewBox="0 0 380 560" role="img" aria-label="Photo of a smiling trainer in a blue shirt holding a tablet in a gym">
      <defs>
        <linearGradient id="trainerTone" x1="0" y1="0" x2="1" y2="1"><stop offset="0" stop-color="#4a4a4a"/><stop offset=".55" stop-color="#3d7fd0"/><stop offset="1" stop-color="#2c5d9c"/></linearGradient>
      </defs>
      <polygon points="150,0 380,0 380,330 240,380 150,300" fill="url(#trainerTone)"/>
    </svg>
    <svg class="layer" viewBox="0 0 380 560" aria-hidden="true">
      <polygon points="0,120 250,20 250,360 0,430" fill="var(--yellow)"/>
      <polygon points="250,20 262,16 262,356 250,360" fill="var(--white)"/>
    </svg>
    <div class="abs programs__rule"></div>
    <h2 class="abs heading programs__title">Tailored programs</h2>
    <p class="abs programs__text">Our programs are structured so that members of all fitness levels feel confident &amp; comfortable during their start-up phase allowing you to quickly build your fitness.</p>

    <div class="abs contact__tab">Contact Us</div>
    <ul class="abs contact__list">
      <li><svg viewBox="0 0 16 16"><path d="M3 1h3l1 4-2 1c1 2 3 4 5 5l1-2 4 1v3c0 1-1 2-2 2C7 15 1 9 1 3c0-1 1-2 2-2z" fill="var(--black)"/></svg>0400 172 639</li>
      <li><svg viewBox="0 0 16 16"><rect x="1" y="3" width="14" height="10" fill="var(--black)"/><path d="M1 3l7 6 7-6" stroke="var(--white)" stroke-width="1.4" fill="none"/></svg>info@punchyard-fit.com.au</li>
      <li><svg viewBox="0 0 16 16"><rect x="1.5" y="3.5" width="11" height="11" fill="none" stroke="var(--black)" stroke-width="1.6"/><path d="M7 9l7-7M9 2h5v5" stroke="var(--black)" stroke-width="1.6" fill="none"/></svg>www.punchyard-fit.com.au</li>
    </ul>
  </div>

  <div class="panel panel--2">
    <svg class="layer" viewBox="0 0 380 560" aria-hidden="true">
      <rect width="380" height="560" fill="var(--charcoal)"/>
    </svg>
    <svg class="layer" viewBox="0 0 380 560" role="img" aria-label="Black and white photo of a boxer throwing a punch, fading into the dark background">
      <defs>
        <radialGradient id="boxerTone" cx=".55" cy=".6" r=".5"><stop offset="0" stop-color="#5a5a5a"/><stop offset="1" stop-color="#2a2a2a" stop-opacity="0"/></radialGradient>
      </defs>
      <rect y="180" width="380" height="380" fill="url(#boxerTone)"/>
    </svg>
    <svg class="layer" viewBox="0 0 380 560" aria-hidden="true">
      <path d="M0,0 L22,0 Q10,280 40,560 L0,560 Z" fill="var(--white)"/>
      <path d="M0,0 L12,0 Q0,280 28,560 L0,560 Z" fill="var(--yellow)"/>
      <path d="M380,0 L352,0 Q376,200 350,560 L380,560 Z" fill="var(--white)"/>
      <path d="M380,0 L364,0 Q386,200 362,560 L380,560 Z" fill="var(--yellow)"/>
    </svg>
    <div class="abs offer">
      <div class="heading offer__lead">Unlimited</div>
      <div class="offer__sub">outdoor boxing classes</div>
      <div class="offer__price">$14.95</div>
      <p class="offer__note">Complete affordability<br>&amp; No judgements guaranteed</p>
      <div class="offer__dash"></div>
    </div>
    <h1 class="abs heading headline">
      <span class="headline__big">Get fit</span>
      <span class="headline__small">lose weight &amp; feel great</span>
    </h1>
  </div>

  <div class="panel panel--3">
    <svg class="layer" viewBox="0 0 380 560" role="img" aria-label="Faint photo of a boxer training outdoors">
      <defs>
        <linearGradient id="coverTone" x1="0" y1="0" x2="0" y2="1"><stop offset="0" stop-color="#f3f3f3"/><stop offset=".6" stop-color="#e2e2e2"/><stop offset="1" stop-color="#9a9a9a"/></linearGradient>
      </defs>
      <rect width="380" height="560" fill="url(#coverTone)"/>
    </svg>
    <svg class="layer" viewBox="0 0 380 560" aria-hidden="true">
      <path d="M0,0 L34,0 Q58,260 20,560 L0,560 Z" fill="var(--yellow)"/>
      <path d="M0,0 L18,0 Q42,260 6,560 L0,560 Z" fill="var(--white)"/>
    </svg>
    <div class="abs brand">
      <span class="brand__mark"></span>
      <span class="brand__name">JAB YARD</span>
    </div>
  </div>
</section>

<section class="sheet sheet--inside" aria-label="Brochure inside">

  <div class="panel panel--1">
    <svg class="layer" viewBox="0 0 380 560" role="img" aria-label="Photo of a woman stretching outdoors in warm sunlight">
      <defs>
        <linearGradient id="stretchTone" x1="0" y1="0" x2="1" y2="1"><stop offset="0" stop-color="#b9a873"/><stop offset="1" stop-color="#6f7a3a"/></linearGradient>
      </defs>
      <rect width="380" height="280" fill="url(#stretchTone)"/>
    </svg>
    <svg class="layer" viewBox="0 0 380 560" role="img" aria-label="Photo of a man doing a plank on green grass">
      <defs>
        <linearGradient id="plankTone" x1="0" y1="0" x2="0" y2="1"><stop offset="0" stop-color="#4f6a2c"/><stop offset="1" stop-color="#7d9a34"/></linearGradient>
      </defs>
      <polygon points="0,300 380,190 380,560 0,560" fill="url(#plankTone)"/>
      <rect y="400" width="380" height="160" fill="#233012" opacity=".45"/>
    </svg>
    <svg class="layer" viewBox="0 0 380 560" aria-hidden="true">
      <polygon points="0,80 380,60 380,170 0,185" fill="var(--yellow)" opacity=".82"/>
      <polygon points="0,292 380,182 380,194 0,304" fill="var(--yellow)"/>
    </svg>
    <div class="abs injury">
      <h3 class="heading feature__title">Injury prevention</h3>
      <p class="feature__text">Our training systems include techniques that will help you avoid injuries and build balanced strength.</p>
    </div>
    <div class="abs core">
      <h3 class="heading feature__title">Strengthen &amp; Tone your core</h3>
      <p class="feature__text">You're core muscles are some of you're most important muscles. Each workout you do incorporates core exercises to help avoid injuries and make you're total body stronger.</p>
    </div>
  </div>

  <div class="panel panel--2">
    <svg class="layer" viewBox="0 0 380 560" aria-hidden="true">
      <rect width="380" height="560" fill="var(--black)"/>
    </svg>
    <svg class="layer" viewBox="0 0 380 560" role="img" aria-label="Black and white photo of a woman in a boxing stance with gloves raised">
      <defs>
        <radialGradient id="fighterTone" cx=".5" cy=".5" r=".5"><stop offset="0" stop-color="#8a8a8a"/><stop offset=".7" stop-color="#3a3a3a"/><stop offset="1" stop-color="#000" stop-opacity="0"/></radialGradient>
      </defs>
      <rect x="20" y="140" width="300" height="260" fill="url(#fighterTone)"/>
    </svg>
    <svg class="layer" viewBox="0 0 380 560" aria-hidden="true">
      <polygon points="0,0 10,0 0,30" fill="var(--yellow)"/>
      <polygon points="340,0 380,0 380,560 300,560" fill="var(--yellow)"/>
      <polygon points="332,0 342,0 302,560 292,560" fill="var(--white)"/>
    </svg>
    <div class="abs energy">
      <h3 class="heading feature__title">Wake up with more energy</h3>
      <p class="feature__text">Every class you'll do will have you filled with energy the will pump you up for the rest of your day.</p>
    </div>
    <div class="abs sleep">
      <h3 class="heading feature__title">Sleep better</h3>
      <p class="feature__text">One of the best parts of exercise is the benefit it has on your sleeping patterns.</p>
      <p class="feature__text">You'll sleep deeper &amp; more sound.</p>
    </div>
  </div>

  <div class="panel panel--3">
    <svg class="layer" viewBox="0 0 380 560" aria-hidden="true">
      <defs>
        <linearGradient id="signTone" x1="0" y1="0" x2="0" y2="1"><stop offset="0" stop-color="var(--yellow)"/><stop offset="1" stop-color="var(--yellow-deep)"/></linearGradient>
      </defs>
      <rect width="380" height="560" fill="url(#signTone)"/>
    </svg>
    <svg class="layer" viewBox="0 0 380 560" role="img" aria-label="Photo of a smiling woman and two hands clasped in encouragement, washed in yellow">
      <defs>
        <radialGradient id="supportTone" cx=".45" cy=".5" r=".55"><stop offset="0" stop-color="#fff7b8"/><stop offset="1" stop-color="var(--yellow)" stop-opacity="0"/></radialGradient>
      </defs>
      <rect y="300" width="380" height="260" fill="url(#supportTone)"/>
    </svg>
    <svg class="layer" viewBox="0 0 380 560" aria-hidden="true">
      <polygon points="0,0 14,0 0,40" fill="var(--black)"/>
      <polygon points="0,510 30,560 0,560" fill="var(--black)"/>
    </svg>
    <div class="abs signup">
      <svg class="signup__icon" viewBox="0 0 44 50" aria-hidden="true">
        <path d="M3 3h28l10 10v34H3z" fill="none" stroke="var(--black)" stroke-width="3"/>
        <path d="M10 18h24M10 26h24M10 34h18" stroke="var(--black)" stroke-width="3"/>
      </svg>
      <h3 class="heading signup__title">Sign up Today!</h3>
      <div class="signup__rule"></div>
      <div class="signup__label">COUPON CODE</div>
      <div class="heading signup__code">SwingHigh27</div>
    </div>
    <div class="abs support__rule"></div>
    <p class="abs support__text">At JAB YARD you'll be surrounded by trainers &amp; other members who are there to encourage &amp; motivate you to reach your goals and to get you moving more.</p>
    <div class="abs support__band"></div>
    <h3 class="abs heading support__title">Supportive environment</h3>
  </div>
</section>

</body>
</html>
```